Business Cards for Corvantis LLC

We need business cards for a new company called “Corvantis LLC”. This is a technology process improvement company providing a comprehensive assessment of the technology used to run their business. The documentation and review process delivers the visibility and reassurance they need to protect their business and plan for the future. The product is called “Halvorne Ledgerwork”. Our primary target is small-medium size businesses, with the deliverables going to the decision maker. We would like to see the designs use the color blue. Our tag line is PROTECT YOUR BUSINESS · TAKE CONTROL OF IT.

Industry/Entity Type

Business

Contact Information for Business Card

Tag line should be on back of card - it does not have to be upper case.

Requirements
Must have
• Please use information when laying out card:
• Name: Darnell Pruitt
• Title: Partner
• Phone Number: (877)555-0143
• Email: dell@corvantisllc.com
• Website: http://corvantisllc.com

```html
<!DOCTYPE html>
<html lang="en">
<head>
<meta charset="utf-8">
<title>Corvantis LLC — Business Cards</title>
<link rel="stylesheet" href="https://fonts.googleapis.com/css2?family=Exo+2:wght@700&family=Open+Sans:wght@400;600;700&display=swap">
<style>
  :root {
    --blue: #1d6fbf;
    --blue-light: #2489cf;
    --blue-dark: #1762ad;
    --grey: #7c7c7c;
    --grey-text: #8a8a8a;
    --ink: #3f4a5a;
    --white: #ffffff;
    --backdrop: #2b2b2d;
  }
  * { margin: 0; padding: 0; box-sizing: border-box; }
  html, body { width: 1200px; height: 900px; overflow: hidden; }
  body {
    background: var(--backdrop);
    font-family: "Open Sans", sans-serif;
    position: relative;
  }
  .card {
    position: absolute;
    width: 560px;
    height: 320px;
    border-radius: 26px;
    overflow: hidden;
    left: 320px;
  }
  /* Back of card */
  .card-back {
    top: 100px;
    background: linear-gradient(135deg, var(--blue-dark) 0%, var(--blue) 45%, var(--blue-light) 100%);
    color: var(--white);
    display: flex;
    flex-direction: column;
    align-items: center;
    justify-content: center;
    gap: 34px;
  }
  .wordmark {
    display: flex;
    align-items: center;
    gap: 14px;
    font-family: "Open Sans", sans-serif;
    font-weight: 700;
    letter-spacing: 1px;
  }
  .wordmark-square { width: 30px; height: 30px; }
  .card-back .wordmark { font-size: 46px; color: var(--white); }
  .card-back .wordmark-square { width: 40px; height: 40px; background: var(--white); }
  .tagline {
    font-size: 15px;
    font-weight: 600;
    letter-spacing: 1.4px;
  }
  /* Front of card */
  .card-front {
    top: 480px;
    background: var(--white);
  }
  .card-front .wordmark {
    position: absolute;
    top: 42px;
    left: 200px;
    font-size: 32px;
    color: var(--blue);
  }
  .card-front .wordmark-square { background: var(--blue); }
  .rule-long {
    position: absolute;
    left: 262px; top: 172px;
    width: 266px; height: 2px;
    background: var(--blue);
  }
  .holder-name {
    position: absolute;
    left: 40px; top: 150px;
    font-family: "Exo 2", sans-serif;
    font-weight: 700;
    font-size: 26px;
    color: var(--blue);
    letter-spacing: 0.5px;
  }
  .holder-title {
    position: absolute;
    left: 42px; top: 188px;
    font-size: 14px;
    font-weight: 700;
    color: var(--grey-text);
  }
  .rule-short {
    position: absolute;
    left: 40px; top: 212px;
    width: 196px; height: 2px;
    background: var(--blue);
  }
  .contact-list {
    position: absolute;
    left: 40px; top: 226px;
    list-style: none;
    font-size: 14px;
    color: var(--ink);
    line-height: 24px;
  }
  .contact-list li { display: flex; align-items: center; gap: 14px; }
  .contact-list svg { width: 16px; height: 14px; fill: var(--blue); }
  .band { position: absolute; left: 0; bottom: 0; }
  .website {
    position: absolute;
    right: 26px; bottom: 14px;
    font-size: 14px;
    color: var(--white);
    letter-spacing: 0.3px;
  }
</style>
</head>
<body>
  <section class="card card-back" aria-label="Back of card">
    <div class="wordmark"><span class="wordmark-square"></span>Corvantis LLC</div>
    <p class="tagline">Protect your business - take control of it.</p>
  </section>

  <section class="card card-front" aria-label="Front of card">
    <div class="wordmark"><span class="wordmark-square"></span>Corvantis LLC</div>
    <div class="rule-long"></div>
    <h1 class="holder-name">DARNELL PRUITT</h1>
    <p class="holder-title">PARTNER</p>
    <div class="rule-short"></div>
    <ul class="contact-list">
      <li>
        <svg viewBox="0 0 16 14" aria-hidden="true"><path d="M1 4c0-2 3-3 7-3s7 1 7 3v1h-4V3.5H5V5H1zM3 6h10l2 7H1z"/></svg>
        (877)555-0143
      </li>
      <li>
        <svg viewBox="0 0 16 14" aria-hidden="true"><path d="M0 2h16v10H0zM1.5 3.2 8 8l6.5-4.8v-.2h-13z" fill-rule="evenodd"/></svg>
        dell@corvantisllc.com
      </li>
    </ul>
    <svg class="band" width="560" height="70" viewBox="0 0 560 70" aria-hidden="true">
      <path d="M0 40 H322 L314 52 H0 Z" fill="var(--grey)"/>
      <path d="M0 58 H330 C340 58 342 54 342 46 V30 C342 20 348 16 360 16 H560 V70 H0 Z" fill="var(--blue)"/>
    </svg>
    <p class="website">www.corvantisllc.com</p>
  </section>
</body>
</html>
```